32 x 24 Swinging Real Estate Yard Sign

We are looking to design a new sign for our business to focus on the remodeling of homes to sell. We are looking to have a yard sign that gets peoples attention and is informational. The headline will be "The Secret to Top Dollar? Remodel First.". We remodel homes for sellers with no up front cost, as they simply pay at closing. This link has more info, https://brightkeelhomes.com/Remodel
The message we want to convey to those seeing the sign is we are a one stop shop, who can renovate your home and sell it for no stress. We are licensed real estate agents and licensed contractors.
Both of these license numbers and info need to be on the design:
CADRE #07264918
Contractors License #2851736
Email: info@brightkeelhomes.com
Phone: (408)555-0183
I'll attach a sample sign we have for our agents normally as well as all brand art work.
• Pantone Colors
o #172A41
Dark blue
o #4381B1
Medium blue
o #6FA6CC
Light blue
Target Market(s)
Residential Real Estate Sellers
Industry/Entity Type
Real Estate
Colors
Designer to choose colors to be used in the design.

```html
<!DOCTYPE html>
<html lang="en">
<head>
<meta charset="UTF-8">
<title>Brightkeel Homes – Remodel First Yard Sign</title>
<link href="https://fonts.googleapis.com/css2?family=Bebas+Neue&family=Montserrat:wght@600;700;800&family=Oswald:wght@500&display=swap" rel="stylesheet">
<style>
  :root {
    --navy: #172A41;
    --mid-blue: #4381B1;
    --light-blue: #6FA6CC;
    --white: #FFFFFF;
    --backdrop: #E8ECF0;
  }
  * { margin: 0; padding: 0; box-sizing: border-box; }
  html, body {
    width: 1200px;
    height: 1200px;
    overflow: hidden;
    background: var(--backdrop);
  }
  .canvas {
    position: relative;
    width: 1200px;
    height: 1200px;
  }
  .yard-sign {
    position: absolute;
    left: 220px;
    top: 97px;
    width: 760px;
    height: 1005px;
    background: var(--mid-blue);
    padding: 16px 16px 0;
  }
  .message-panel {
    position: relative;
    width: 728px;
    height: 800px;
    background: var(--navy);
    text-align: center;
  }
  .brand-dot {
    position: absolute;
    left: 50%;
    top: 62px;
    width: 86px;
    height: 86px;
    margin-left: -43px;
    border-radius: 50%;
    background: var(--light-blue);
  }
  .brand-name {
    position: absolute;
    left: 0;
    right: 0;
    top: 190px;
    font-family: 'Montserrat', sans-serif;
    font-weight: 600;
    font-size: 50px;
    letter-spacing: 2px;
    color: var(--white);
  }
  .divider {
    position: absolute;
    left: 54px;
    right: 54px;
    top: 325px;
    height: 1px;
    background: rgba(111, 166, 204, 0.45);
  }
  .headline {
    position: absolute;
    left: 0;
    right: 0;
    top: 340px;
    font-family: 'Bebas Neue', sans-serif;
    font-size: 134px;
    line-height: 124px;
    color: var(--white);
    text-shadow: 3px 3px 0 rgba(0, 0, 0, 0.35);
  }
  .headline .call-to-action {
    display: block;
    color: var(--mid-blue);
    text-shadow: none;
  }
  .license {
    position: absolute;
    bottom: 24px;
    font-family: 'Oswald', sans-serif;
    font-weight: 500;
    font-size: 22px;
    letter-spacing: 0.5px;
    color: var(--white);
    text-transform: uppercase;
  }
  .license--realty { left: 16px; }
  .license--contractor { right: 14px; bottom: 40px; }
  .contact-band {
    height: 189px;
    text-align: center;
    padding-top: 18px;
  }
  .phone {
    display: block;
    font-family: 'Montserrat', sans-serif;
    font-weight: 800;
    font-size: 72px;
    line-height: 92px;
    color: var(--white);
    text-shadow: 4px 4px 0 var(--navy);
  }
  .email {
    display: block;
    margin-top: 8px;
    font-family: 'Montserrat', sans-serif;
    font-weight: 700;
    font-size: 33px;
    letter-spacing: 2px;
    color: var(--navy);
    text-transform: uppercase;
  }
</style>
</head>
<body>
  <main class="canvas">
    <section class="yard-sign">
      <div class="message-panel">
        <span class="brand-dot" aria-hidden="true"></span>
        <p class="brand-name">BRIGHTKEEL HOMES</p>
        <div class="divider"></div>
        <h1 class="headline">
          The Secret to<br>Top Dollar?
          <span class="call-to-action">Remodel First</span>
        </h1>
        <p class="license license--realty">CADRE #07264918</p>
        <p class="license license--contractor">Contractors License #2851736</p>
      </div>
      <div class="contact-band">
        <span class="phone">(408) 555-0183</span>
        <span class="email">info@brightkeelhomes.com</span>
      </div>
    </section>
  </main>
</body>
</html>
```